Tov Fiesta Mariners

We are party planning business. We are a team of established individuals and business in party stream businesses like DJ, Caterers, Party supplies, Kids parties, Events & Private Parties and much more. So basically me and business collaborate a team of business or individuals to do clients party in the best way possible.

Target Market(s)

majority of them 16 to 30 -60% to 70 % and 30 to 40 year olds- 30% to 40 %

Industry/Entity Type

Party Planning

Contact Information for Business Card

Tov
Owner & Manager
0471829354
tovfiestamariners@mailpost.example

Requirements
Must have
• front side : Logo and list of services we provide
DJ's, Catering,All party supplies, Tinyjubilee and more...just to show what the business is about when anyone looks at the card and at the rear side my details which are already provided.
Should not have
• Dont make it look we do kids party which is just one of the things we do but don't make my business card look like kids party specialist make it more connecting to youngsters and older crowd more

```html
<!DOCTYPE html>
<html lang="en">
<head>
<meta charset="utf-8">
<title>Tov Fiesta Mariners – Business Card</title>
<link rel="stylesheet" href="https://fonts.googleapis.com/css2?family=Pirata+One&display=swap">
<style>
  :root {
    --backdrop: #e8e5e0;
    --card-black: #0b0b0b;
    --card-white: #ffffff;
    --accent-red: #d2232a;
    --ink: #111111;
    --text-light: #f4f4f4;
  }
  * { box-sizing: border-box; margin: 0; padding: 0; }
  html, body {
    width: 1200px;
    height: 784px;
    overflow: hidden;
    background: var(--backdrop);
    font-family: "Pirata One", fantasy;
  }
  .canvas {
    position: relative;
    width: 1200px;
    height: 784px;
  }
  .card {
    position: absolute;
    top: 95px;
    width: 340px;
    height: 595px;
    overflow: hidden;
    box-shadow: 0 6px 18px rgba(0,0,0,0.18);
  }
  .card--back { left: 170px; background: var(--card-black); }
  .card--front { left: 690px; background: var(--card-white); }

  /* back side */
  .contact {
    position: absolute;
    top: 70px;
    left: 0;
    width: 100%;
    text-align: center;
    color: var(--text-light);
  }
  .contact__name {
    color: var(--accent-red);
    font-size: 40px;
    line-height: 1.1;
  }
  .contact__role { font-size: 24px; margin-top: 8px; }
  .contact__phone { font-size: 34px; margin-top: 10px; letter-spacing: 1px; }
  .contact__email { font-size: 17px; margin-top: 10px; }

  /* front side */
  .brand {
    position: absolute;
    top: 60px;
    left: 0;
    width: 100%;
    text-align: center;
  }
  .brand__dot {
    display: block;
    width: 54px;
    height: 54px;
    margin: 0 auto 18px;
    border-radius: 50%;
    background: var(--accent-red);
  }
  .brand__name {
    color: var(--ink);
    font-size: 34px;
    font-weight: 400;
    line-height: 1.1;
  }
  .brand__tagline {
    color: var(--ink);
    font-size: 20px;
    line-height: 1.2;
    margin-top: 18px;
  }
  .front-base {
    position: absolute;
    left: 0;
    bottom: 0;
    width: 340px;
    height: 300px;
  }
  .services {
    position: absolute;
    left: 0;
    bottom: 60px;
    width: 100%;
    list-style: none;
    text-align: center;
    color: var(--text-light);
    font-size: 27px;
    line-height: 1.5;
  }
</style>
</head>
<body>
<main class="canvas">

  <section class="card card--back" aria-label="Card back">
    <div class="contact">
      <p class="contact__name">Tov</p>
      <p class="contact__role">Owner &amp; Manager</p>
      <p class="contact__phone">0471829354</p>
      <p class="contact__email">tovfiestamariners@mailpost.example</p>
    </div>
  </section>

  <section class="card card--front" aria-label="Card front">
    <div class="brand">
      <span class="brand__dot" aria-hidden="true"></span>
      <h1 class="brand__name">Tov Fiesta Mariners</h1>
      <p class="brand__tagline">Bringing A Crew Of Experts<br>To Every Celebration</p>
    </div>
    <svg class="front-base" viewBox="0 0 340 300" aria-hidden="true">
      <path d="M0 0 Q170 95 340 0 L340 300 L0 300 Z" fill="var(--card-black)"/>
      <path d="M0 0 Q170 95 340 0" fill="none" stroke="var(--accent-red)" stroke-width="6"/>
    </svg>
    <ul class="services">
      <li>DJ's</li>
      <li>Catering</li>
      <li>All party supplies</li>
      <li>Tinyjubilee and more...</li>
    </ul>
  </section>

</main>
</body>
</html>
```